business card - for laser marking

I need design (curve) for my business card (make with laser) size 85mm x 55mm. How it look business card with laser marking see attached picture.

color:
Background: white
text and icons black

Please include: one side
1. dominik vrhovec - direktor
2. phone: +386(0)41 726 193
+386(0)592 817 06
3. info@zlatorez.example
4. faecebook.com/Zlatorez.Ex
5. KP-ATELJE, Dominik Vrhovec s.p.
Brezova ulica 17, 1000 Ljubljana, SI
6. logo

Please include: second side
1. logo
2. www.zlatorez.example
3. Lasersko graviranje
ovitki telefonov, ohišja telefonov / tablic, nakit, ure, alu vizitke, dog-tagi, kemični svinčniki, orodja, noži, vžigalniki

Industry/Entity Type

Business

Contact Information for Business Card

Please include: one side
+386(0)592 817 06
3. info@zlatorez.example
6. logo

1. logo
2. www.zlatorez.example
3. Lasersko graviranje

Colors
000000
ffffff

Requirements
Must have
• I need design (curve) for my business card (make with laser) size 85mm x 55mm. How it look business card with laser marking see attached picture.
• color:
• Background: white
• text and icons black
• Please include: one side
• 1. dominik vrhovec - direktor
• 2. phone: +386(0)41 726 193
• +386(0)592 817 06
• 3. info@zlatorez.example
• 4. faecebook.com/Zlatorez.Ex
• 5. KP-ATELJE, Dominik Vrhovec s.p.
• Brezova ulica 17, 1000 Ljubljana, SI
• 6. logo
• Please include: second side
• 1. logo
• 2. www.zlatorez.example
• 3. Lasersko graviranje
• ovitki telefonov, ohišja telefonov / tablic, nakit, ure, alu vizitke, dog-tagi, kemični svinčniki, orodja, noži, vžigalniki

```html
<!DOCTYPE html>
<html lang="sl">
<head>
<meta charset="utf-8">
<title>Zlatorez – vizitka</title>
<link rel="stylesheet" href="https://fonts.googleapis.com/css2?family=Exo+2:wght@300;400;600&display=swap">
<style>
  :root {
    --backdrop: #c4c4c7;
    --card: #ffffff;
    --ink: #1c1c1c;
    --ink-soft: #3a3a3a;
    --brand-pink: #c4325e;
    --brand-green: #7fa653;
  }
  * { box-sizing: border-box; margin: 0; padding: 0; }
  html, body { width: 1200px; height: 1200px; overflow: hidden; }
  body {
    background: var(--backdrop);
    font-family: "Exo 2", sans-serif;
    color: var(--ink);
    position: relative;
  }
  .card {
    position: absolute;
    top: 250px;
    width: 440px;
    height: 680px;
    background: var(--card);
    box-shadow: 0 14px 40px rgba(0,0,0,.18);
  }
  .card--front { left: 110px; }
  .card--back  { left: 650px; }

  .brand {
    position: absolute;
    top: 140px;
    left: 0; right: 0;
    display: flex;
    align-items: center;
    justify-content: center;
    gap: 14px;
  }
  .brand__dot {
    width: 22px; height: 22px;
    border-radius: 50%;
    background: var(--brand-green);
  }
  .brand__name {
    font-weight: 600;
    font-size: 46px;
    letter-spacing: 1px;
    color: var(--brand-pink);
  }

  /* front side */
  .person {
    position: absolute;
    right: 60px;
    top: 310px;
    text-align: right;
  }
  .person__name {
    font-weight: 300;
    font-size: 27px;
    letter-spacing: .5px;
    text-transform: uppercase;
  }
  .person__role {
    font-weight: 300;
    font-size: 16px;
    color: var(--ink-soft);
    margin-top: 2px;
  }
  .contacts {
    position: absolute;
    right: 48px;
    top: 430px;
    list-style: none;
    text-align: right;
    font-weight: 300;
    font-size: 18px;
    line-height: 26px;
  }
  .contacts li { display: flex; justify-content: flex-end; align-items: center; gap: 10px; }
  .contacts .gap { margin-top: 16px; }
  .icon { width: 14px; height: 14px; flex: none; }
  .icon--square { background: var(--ink-soft); border-radius: 2px; }
  .address {
    position: absolute;
    right: 48px;
    bottom: 70px;
    text-align: right;
    font-style: normal;
    font-weight: 300;
    font-size: 17px;
    line-height: 24px;
  }
  .address__line { display: flex; justify-content: flex-end; align-items: center; gap: 10px; }

  /* back side */
  .services {
    position: absolute;
    left: 60px;
    top: 330px;
  }
  .services__title {
    font-weight: 400;
    font-size: 21px;
    margin-bottom: 12px;
  }
  .services__list {
    list-style: none;
    padding-left: 12px;
    font-weight: 300;
    font-size: 16px;
    line-height: 32px;
  }
  .website {
    position: absolute;
    left: 60px;
    bottom: 70px;
    display: flex;
    align-items: center;
    gap: 12px;
    font-weight: 400;
    font-size: 26px;
  }
  .website svg { width: 28px; height: 28px; }
</style>
</head>
<body>

<section class="card card--front" aria-label="Sprednja stran vizitke">
  <div class="brand">
    <span class="brand__name">ZLATOREZ</span>
    <span class="brand__dot"></span>
  </div>

  <div class="person">
    <p class="person__name">Dominik&nbsp;&nbsp;Vrhovec</p>
    <p class="person__role">direktor</p>
  </div>

  <ul class="contacts">
    <li>+386(0)41 726 193
      <svg class="icon" viewBox="0 0 24 24" aria-hidden="true"><path fill="currentColor" d="M6.6 10.8a15 15 0 0 0 6.6 6.6l2.2-2.2a1 1 0 0 1 1-.25 11.4 11.4 0 0 0 3.6.57 1 1 0 0 1 1 1V20a1 1 0 0 1-1 1A17 17 0 0 1 3 4a1 1 0 0 1 1-1h3.5a1 1 0 0 1 1 1c0 1.25.2 2.45.57 3.57a1 1 0 0 1-.25 1z"/></svg></li>
    <li>+386(0)592 817 06
      <svg class="icon" viewBox="0 0 24 24" aria-hidden="true"><path fill="currentColor" d="M6.6 10.8a15 15 0 0 0 6.6 6.6l2.2-2.2a1 1 0 0 1 1-.25 11.4 11.4 0 0 0 3.6.57 1 1 0 0 1 1 1V20a1 1 0 0 1-1 1A17 17 0 0 1 3 4a1 1 0 0 1 1-1h3.5a1 1 0 0 1 1 1c0 1.25.2 2.45.57 3.57a1 1 0 0 1-.25 1z"/></svg></li>
    <li class="gap">Zlatorez.Ex <span class="icon icon--square"></span></li>
    <li>info@zlatorez.example
      <svg class="icon" viewBox="0 0 24 24" aria-hidden="true"><rect x="2" y="5" width="20" height="14" rx="1" fill="currentColor"/><path d="M3 6l9 7 9-7" stroke="#fff" stroke-width="1.6" fill="none"/></svg></li>
  </ul>

  <address class="address">
    <span class="address__line">KP-ATELJE, Dominik Vrhovec s.p.
      <svg class="icon" viewBox="0 0 24 24" aria-hidden="true"><path fill="currentColor" d="M12 2a7 7 0 0 0-7 7c0 5 7 13 7 13s7-8 7-13a7 7 0 0 0-7-7zm0 9.5A2.5 2.5 0 1 1 12 6.5a2.5 2.5 0 0 1 0 5z"/></svg></span>
    <span class="address__line">Brezova ulica 17, 1000 Ljubljana, SI</span>
  </address>
</section>

<section class="card card--back" aria-label="Zadnja stran vizitke">
  <div class="brand">
    <span class="brand__name">ZLATOREZ</span>
    <span class="brand__dot"></span>
  </div>

  <div class="services">
    <h2 class="services__title">Lasersko graviranje</h2>
    <ul class="services__list">
      <li>ovitki telefonov</li>
      <li>ohišja telefonov / tablic</li>
      <li>nakit, ure, alu vizitke</li>
      <li>dog-tagi</li>
      <li>kemični svinčniki</li>
      <li>orodja, noži, vžigalniki</li>
    </ul>
  </div>

  <p class="website">
    <svg viewBox="0 0 24 24" aria-hidden="true" fill="none" stroke="currentColor" stroke-width="1.4"><circle cx="12" cy="12" r="10"/><ellipse cx="12" cy="12" rx="4.5" ry="10"/><path d="M2 12h20M4 6.5h16M4 17.5h16"/></svg>
    www.zlatorez.example
  </p>
</section>

</body>
</html>
```